Instagram adverts for international jewellery making school

We need 10 single image Instagram adverts to promote our jewellery school in Kuala Lumpur Malaysia to an international market. The images should all have a different feel and it is up to the designer to also come up with wording to include on the images - you can refer to our website for details on the classes https://marthadenbyjewellery.com/firststeps-1. <br/><br/>The feeling and wording should be fun, vibrant and quirky - no need to be too serious here, and I generally prefer busier images - they won't be used for promotional posts so no need to worry about Instagram / FB ad restrictions<br/><br/>We have attached an example of one Instagram ad we created ourselves for reference.<br/><br/>We only need to see one advert before selecting you as a designer and we are looking to build an ongoing relationship for all future graphic design needs. <br/><br/>We will send a google drive of images to the chosen designer but for now, please just use the images from the website for the prototype.

Font styles to use
Serif
Sans Serif

Colors

Designer to choose colors to be used in the design.

Requirements
Must have
• Fun bold vibrant feel
Nice to have
• Multiple images included in each post

```html
<!DOCTYPE html>
<html lang="en">
<head>
<meta charset="UTF-8">
<title>So You Want To Be A Jewellery Designer – Instagram Advert</title>
<link rel="stylesheet" href="https://fonts.googleapis.com/css2?family=Cinzel:wght@400&family=Montserrat:wght@400&display=swap">
<style>
  :root {
    --band-edge: #c98a2e;
    --band-mid: #f6a94a;
    --band-light: #fbc27a;
    --gold: #d39a40;
    --ink: #4a4646;
    --muted: #8a8a8a;
    --paper: #ffffff;
  }
  * { margin: 0; padding: 0; box-sizing: border-box; }
  html, body { width: 1200px; height: 1200px; overflow: hidden; background: var(--paper); }
  .advert { position: relative; width: 1200px; height: 1200px; background: var(--paper); }

  .band {
    position: absolute; left: 0; width: 1200px; height: 100px;
    background: linear-gradient(180deg, var(--band-edge) 0%, var(--band-mid) 30%, var(--band-light) 50%, var(--band-mid) 72%, var(--band-edge) 100%);
  }
  .band--top { top: 0; }
  .band--bottom { bottom: 0; }

  .frame {
    position: absolute; border: 4px solid var(--gold);
  }
  .frame--back { left: 385px; top: 205px; width: 420px; height: 420px; transform: rotate(-9deg); }
  .frame--front { left: 385px; top: 205px; width: 420px; height: 420px; transform: rotate(14deg); }

  .photo { position: absolute; }
  .photo--hero {
    left: 470px; top: 262px; width: 240px; height: 300px; border-radius: 60px 60px 80px 80px;
    background: radial-gradient(ellipse at 45% 38%, #9a3048 0%, #6b1a2c 45%, #4a3a3e 70%, #b9b6b6 100%);
  }
  .photo--thumb {
    left: 282px; top: 895px; width: 104px; height: 122px; border-radius: 24px;
    background: radial-gradient(ellipse at 45% 40%, #8c2a40 0%, #5e1a2a 55%, #a9a6a8 100%);
  }
  .photo--rings {
    left: 412px; top: 880px; width: 326px; height: 142px; border-radius: 30px;
    background: linear-gradient(90deg, #b0453a 0%, #e8c24a 25%, #c9cfd6 45%, #5c9a6a 62%, #c23a52 78%, #6b6b6b 100%);
    opacity: 0.85;
  }

  .headline {
    position: absolute; left: 343px; top: 742px;
    font-family: "Cinzel", serif; font-weight: 400; font-size: 44px; line-height: 54px;
    color: var(--ink); letter-spacing: 1px;
  }

  .brand-name {
    position: absolute; left: 790px; top: 935px; width: 210px; text-align: center;
    font-family: "Cinzel", serif; font-weight: 400; font-size: 24px; line-height: 30px;
    color: var(--ink);
  }

  .note {
    position: absolute; left: 0; top: 1058px; width: 1200px; text-align: center;
    font-family: "Montserrat", sans-serif; font-weight: 400; font-size: 15px; line-height: 19px;
    color: var(--muted);
  }
</style>
</head>
<body>
<main class="advert">
  <div class="band band--top"></div>

  <div class="frame frame--back"></div>
  <div class="frame frame--front"></div>

  <div class="photo photo--hero" role="img" aria-label="Silver ring set with a large cushion-cut ruby"></div>

  <h1 class="headline">So You Want To Be A<br>Jewellery Design ?</h1>

  <div class="photo photo--thumb" role="img" aria-label="Small view of the ruby ring"></div>
  <div class="photo photo--rings" role="img" aria-label="Row of stacking rings set with coloured gemstones"></div>

  <p class="brand-name">Martha Denby</p>

  <p class="note">new dates just listed for 4-week intensive<br>kickstarter programme !</p>

  <div class="band band--bottom"></div>
</main>
</body>
</html>
```